Flyer for a Payroll and Bookkeeping Companmy

Need a brochure to highlight our costs and service to hand out to clients.

Please see attachments for more information.

It Service

```html
<!DOCTYPE html>
<html lang="en">
<head>
<meta charset="utf-8">
<title>Harbor Ridge – Pricing Flyers</title>
<link rel="stylesheet" href="https://fonts.googleapis.com/css2?family=Lato:wght@400;700;900&family=Montserrat:wght@800;900&display=swap">
<style>
  :root{
    --blue:#0b72c4;
    --blue-dark:#075a9c;
    --orange:#e8781e;
    --ink:#2b2b2b;
    --band:#ebebeb;
    --backdrop:#a8a8a8;
    --white:#ffffff;
  }
  *{box-sizing:border-box;margin:0;padding:0}
  html,body{width:1200px;height:1200px;overflow:hidden}
  body{background:var(--backdrop);position:relative;font-family:"Lato",sans-serif;color:var(--ink)}

  .sheet{position:absolute;left:307px;width:838px;height:644px;background:var(--white);
    transform:scale(.8);transform-origin:top left;overflow:hidden}
  .sheet--bookkeeping{top:68px}
  .sheet--payroll{top:629px}

  .brand{position:absolute;display:flex;align-items:center;gap:8px;
    font-family:"Lato",sans-serif;font-weight:900;font-size:24px;color:var(--blue)}
  .brand__dot{width:22px;height:22px;border-radius:50%;background:var(--orange)}

  .title{position:absolute;font-family:"Lato",sans-serif;font-weight:900;letter-spacing:-.3px;white-space:nowrap}
  .title .accent{color:var(--orange)}
  .title .main{color:var(--blue)}

  /* pricing table */
  .col-head{position:absolute;font-size:11px;font-weight:900;letter-spacing:.3px;color:var(--ink)}
  .plans{position:absolute;display:grid;grid-template-columns:repeat(4,1fr);text-align:center}
  .plan__name{font-size:9.5px;font-weight:700;color:var(--ink);white-space:nowrap}
  .plan__price{font-size:12px;font-weight:900;color:var(--orange);line-height:1.1}

  .row{position:absolute;height:92px}
  .row__band{position:absolute;left:0;right:0;top:4px;height:58px;background:var(--band)}
  .row__tab{position:absolute;left:13px;top:0;width:72px;height:90px}
  .row__label{position:absolute;left:13px;top:4px;width:72px;height:58px;display:flex;flex-direction:column;
    align-items:center;justify-content:center;text-align:center;color:var(--white);font-size:10.5px;font-weight:700;line-height:1.2}
  .row__label small{font-size:7px;font-weight:400;opacity:.9}
  .row__cells{position:absolute;right:0;top:4px;height:58px;display:grid;grid-template-columns:repeat(4,1fr);gap:2px}
  .cell{background:var(--band);display:flex;flex-direction:column;align-items:center;justify-content:center;
    text-align:center;font-size:11px;font-weight:700;line-height:1.15;color:var(--ink)}
  .cell .tick{font-size:16px;font-weight:900;line-height:1}
  .cell .note{font-size:9.5px}

  .table--left .row{left:44px;width:340px}
  .table--left .row__cells{width:255px}
  .table--right .row{left:452px;width:342px}
  .table--right .row__cells{width:258px}

  /* footer */
  .footer{position:absolute;left:0;bottom:0;width:838px;height:30px}
  .footer svg{position:absolute;inset:0}
  .footer__info{position:absolute;left:58px;top:0;height:30px;display:flex;align-items:center;gap:28px;
    color:var(--white);font-size:11.5px}
  .footer__info span{display:flex;align-items:center;gap:6px}

  /* payroll sheet */
  .backdrop-photo{position:absolute;inset:0 0 30px 0;
    background:radial-gradient(ellipse at 75% 65%,#e6e6e6 0%,#f4f4f4 40%,#fbfbfb 70%),#fafafa}
  .price-hero{position:absolute;left:0;right:0;text-align:center}
  .price-hero__amount{top:108px;font-family:"Montserrat",sans-serif;font-weight:900;font-size:122px;line-height:1;
    color:var(--orange);text-shadow:2px 4px 3px rgba(0,0,0,.25);letter-spacing:-2px}
  .price-hero__unit{top:232px;font-size:62px;font-weight:400;color:var(--ink);line-height:1}
  .employee-band{position:absolute;left:182px;top:306px;width:510px;height:112px}
  .employee-band__text{position:absolute;left:226px;top:339px;display:flex;align-items:baseline;gap:26px;color:var(--white)}
  .employee-band__text .amount{font-family:"Montserrat",sans-serif;font-weight:900;font-size:52px}
  .employee-band__text .per{font-weight:700;font-size:44px}
  .no-fees{top:446px;font-family:"Montserrat",sans-serif;font-weight:900;font-size:60px;color:var(--orange);letter-spacing:1px}
  .fine-print{position:absolute;left:46px;right:46px;top:546px;text-align:center;font-size:11.5px;line-height:1.5;color:var(--ink)}
  .fine-print .highlight{color:var(--orange)}
</style>
</head>
<body>

<!-- Bookkeeping pricing sheet -->
<section class="sheet sheet--bookkeeping">
  <div class="brand" style="left:64px;top:70px"><span class="brand__dot"></span>Harbor Ridge</div>
  <h1 class="title" style="right:44px;top:34px;font-size:45px"><span class="accent">Bookkeeping</span> <span class="main">Pricing</span></h1>

  <div class="table--left">
    <div class="col-head" style="left:70px;top:148px">SERVICES</div>
    <div class="plans" style="left:129px;top:149px;width:255px">
      <div><div class="plan__name">Premium</div><div class="plan__price">$999</div></div>
      <div><div class="plan__name">Entrepreneur</div><div class="plan__price">$599</div></div>
      <div><div class="plan__name">Growth</div><div class="plan__price">$299</div></div>
      <div><div class="plan__name">Start Up</div><div class="plan__price">$149</div></div>
    </div>

    <div class="row" style="top:171px">
      <div class="row__band"></div>
      <svg class="row__tab" viewBox="0 0 72 90"><polygon points="0,4 66,4 72,0 72,68 36,90 0,68" fill="var(--blue)"/></svg>
      <div class="row__label">Employees</div>
      <div class="row__cells">
        <div class="cell">Around<br>10+</div><div class="cell">Around<br>5-9</div>
        <div class="cell">Around<br>2-5</div><div class="cell">Around<br>1-2</div>
      </div>
    </div>

    <div class="row" style="top:288px">
      <div class="row__band"></div>
      <svg class="row__tab" viewBox="0 0 72 90"><polygon points="0,4 66,4 72,0 72,68 36,90 0,68" fill="var(--orange)"/></svg>
      <div class="row__label">Transactions/<br>Month</div>
      <div class="row__cells">
        <div class="cell">Up to<br>250</div><div class="cell">Up to<br>150</div>
        <div class="cell">Up to<br>75</div><div class="cell">Up to<br>50</div>
      </div>
    </div>

    <div class="row" style="top:405px">
      <div class="row__band"></div>
      <svg class="row__tab" viewBox="0 0 72 90"><polygon points="0,4 66,4 72,0 72,68 36,90 0,68" fill="var(--blue)"/></svg>
      <div class="row__label">Bookkeeping</div>
      <div class="row__cells">
        <div class="cell"><span class="tick">✓</span>Weekly</div><div class="cell"><span class="tick">✓</span>Weekly</div>
        <div class="cell"><span class="tick">✓</span>Monthly</div><div class="cell"><span class="tick">✓</span>Quarterly</div>
      </div>
    </div>

    <div class="row" style="top:512px">
      <div class="row__band"></div>
      <svg class="row__tab" viewBox="0 0 72 90"><polygon points="0,4 66,4 72,0 72,68 36,90 0,68" fill="var(--orange)"/></svg>
      <div class="row__label">Financial<br>Reports<br>&amp; Review</div>
      <div class="row__cells">
        <div class="cell"><span class="tick">✓</span>Monthly</div><div class="cell"><span class="tick">✓</span>Monthly</div>
        <div class="cell"><span class="tick">✓</span>Monthly</div><div class="cell"><span class="tick">✓</span>Quarterly</div>
      </div>
    </div>
  </div>

  <div class="table--right">
    <div class="col-head" style="left:478px;top:149px">SERVICES</div>
    <div class="plans" style="left:536px;top:150px;width:258px">
      <div><div class="plan__name">Premium</div><div class="plan__price">$999</div></div>
      <div><div class="plan__name">Entrepreneur</div><div class="plan__price">$599</div></div>
      <div><div class="plan__name">Growth</div><div class="plan__price">$299</div></div>
      <div><div class="plan__name">Start Up</div><div class="plan__price">$149</div></div>
    </div>

    <div class="row" style="top:171px">
      <div class="row__band"></div>
      <svg class="row__tab" viewBox="0 0 72 90"><polygon points="0,4 66,4 72,0 72,68 36,90 0,68" fill="var(--blue)"/></svg>
      <div class="row__label">Support<small>(Phone and Chat)</small></div>
      <div class="row__cells">
        <div class="cell"><span class="tick">✓</span></div><div class="cell"><span class="tick">✓</span></div>
        <div class="cell"><span class="tick">✓</span></div><div class="cell"><span class="tick">✓</span></div>
      </div>
    </div>

    <div class="row" style="top:288px">
      <div class="row__band"></div>
      <svg class="row__tab" viewBox="0 0 72 90"><polygon points="0,4 66,4 72,0 72,68 36,90 0,68" fill="var(--orange)"/></svg>
      <div class="row__label">Online<br>Collaboration<br>Portal<small>(Shared Drive)</small></div>
      <div class="row__cells">
        <div class="cell"><span class="tick">✓</span></div><div class="cell"><span class="tick">✓</span></div>
        <div class="cell"><span class="tick">✓</span></div><div class="cell"><span class="tick">✓</span></div>
      </div>
    </div>

    <div class="row" style="top:405px">
      <div class="row__band"></div>
      <svg class="row__tab" viewBox="0 0 72 90"><polygon points="0,4 66,4 72,0 72,68 36,90 0,68" fill="var(--blue)"/></svg>
      <div class="row__label">Business<br>Tax Return</div>
      <div class="row__cells">
        <div class="cell"><span class="tick">✓</span></div><div class="cell"><span class="tick">✓</span></div>
        <div class="cell">$799</div><div class="cell">$599</div>
      </div>
    </div>

    <div class="row" style="top:512px">
      <div class="row__band"></div>
      <svg class="row__tab" viewBox="0 0 72 90"><polygon points="0,4 66,4 72,0 72,68 36,90 0,68" fill="var(--orange)"/></svg>
      <div class="row__label">Bill Pay</div>
      <div class="row__cells">
        <div class="cell"><span class="tick">✓</span><span class="note">$5 /<br>Payment</span></div>
        <div class="cell">x</div><div class="cell">x</div><div class="cell">x</div>
      </div>
    </div>
  </div>

  <footer class="footer">
    <svg viewBox="0 0 838 30" preserveAspectRatio="none">
      <polygon points="0,0 561,0 579,30 0,30" fill="var(--blue)"/>
      <polygon points="576,9 838,9 838,30 589,30" fill="var(--orange)"/>
    </svg>
    <div class="footer__info">
      <span><svg width="10" height="10" viewBox="0 0 10 10"><path d="M2 0.5 L3.8 2.6 L2.9 3.8 Q4 6 6.2 7.1 L7.4 6.2 L9.5 8 L8.4 9.5 Q4 9 0.5 1.6 Z" fill="var(--white)"/></svg>555-014-2290</span>
      <span><svg width="10" height="10" viewBox="0 0 10 10"><circle cx="5" cy="5" r="4.3" fill="none" stroke="var(--white)" stroke-width="1.1"/><path d="M0.7 5 H9.3 M5 0.7 Q2 5 5 9.3 M5 0.7 Q8 5 5 9.3" fill="none" stroke="var(--white)" stroke-width="0.9"/></svg>HarborRidge.com</span>
      <span><svg width="8" height="11" viewBox="0 0 8 11"><path d="M4 0 A4 4 0 0 1 8 4 Q8 6.5 4 11 Q0 6.5 0 4 A4 4 0 0 1 4 0 Z" fill="var(--white)"/><circle cx="4" cy="4" r="1.5" fill="var(--blue)"/></svg>1420 Maple Ave, Springfield, OR 97477</span>
    </div>
  </footer>
</section>

<!-- Payroll pricing sheet -->
<section class="sheet sheet--payroll">
  <div class="backdrop-photo" role="img" aria-label="Faded office photo of a person working at a desk with a laptop"></div>
  <div class="brand" style="left:46px;top:72px"><span class="brand__dot"></span>Harbor Ridge</div>
  <h1 class="title" style="right:19px;top:34px;font-size:42px"><span class="accent">Simplified</span> <span class="main">Payroll Pricing</span></h1>

  <div class="price-hero price-hero__amount">$25</div>
  <div class="price-hero price-hero__unit">Per Payroll</div>

  <svg class="employee-band" viewBox="0 0 510 112">
    <polygon points="12,26 510,6 484,112 12,112" fill="#cfcfcf"/>
    <polygon points="0,23 502,2 479,108 0,108" fill="var(--blue)"/>
  </svg>
  <div class="employee-band__text"><span class="amount">+$5</span><span class="per">per Employee</span></div>

  <div class="price-hero no-fees">No Set Up Fees!</div>

  <p class="fine-print">Direct deposit only, add <b>$20</b> per payroll if you elect to have paper checks shipped to you.&nbsp; Minimum charge of two payrolls per month. <span class="highlight">Cost per employee drops to $4 after 20 employees.</span></p>

  <footer class="footer">
    <svg viewBox="0 0 838 30" preserveAspectRatio="none">
      <polygon points="0,0 575,0 593,30 0,30" fill="var(--blue)"/>
      <polygon points="580,9 838,9 838,30 594,30" fill="var(--orange)"/>
    </svg>
    <div class="footer__info">
      <span><svg width="10" height="10" viewBox="0 0 10 10"><path d="M2 0.5 L3.8 2.6 L2.9 3.8 Q4 6 6.2 7.1 L7.4 6.2 L9.5 8 L8.4 9.5 Q4 9 0.5 1.6 Z" fill="var(--white)"/></svg>555-014-2290</span>
      <span><svg width="10" height="10" viewBox="0 0 10 10"><circle cx="5" cy="5" r="4.3" fill="none" stroke="var(--white)" stroke-width="1.1"/><path d="M0.7 5 H9.3 M5 0.7 Q2 5 5 9.3 M5 0.7 Q8 5 5 9.3" fill="none" stroke="var(--white)" stroke-width="0.9"/></svg>HarborRidge.com</span>
      <span><svg width="8" height="11" viewBox="0 0 8 11"><path d="M4 0 A4 4 0 0 1 8 4 Q8 6.5 4 11 Q0 6.5 0 4 A4 4 0 0 1 4 0 Z" fill="var(--white)"/><circle cx="4" cy="4" r="1.5" fill="var(--blue)"/></svg>1420 Maple Ave, Springfield, OR 97477</span>
    </div>
  </footer>
</section>

</body>
</html>
```